Podcast Cover Art for Inspiring Fun Show

Title: The Dave R Hour

I am looking for a simple design that includes the following:

1. Picture of me (the one I attached with the background removed) on a simple background (please refer to attachments for ideas).
2. The title done in professional lettering that is easy to read and stands out on the background

Please see attached pictures for:

1) Other podcast art I like
2) Backgrounds that I like
3) A picture of me (please edit out the background)

Target Market(s)

Anyone into personal-development, inspiring content and motivational stories.

Font styles to use
Sans Serif

Colors

Designer to choose colors to be used in the design.

Requirements
Must have
• - Title "The Dave R Hour" in professional lettering that is large and very easy to read
• - Picture of me on the background

```html
<!DOCTYPE html>
<html lang="en">
<head>
<meta charset="utf-8">
<title>The Dave R Hour — Podcast Cover</title>
<link rel="stylesheet" href="https://fonts.googleapis.com/css2?family=Archivo+Black&display=swap">
<style>
  :root {
    --sky: #cdeaf7;
    --ink: #0d2f45;
    --coral: #e8705f;
    --amber: #f2b33d;
    --leaf: #9fcf5a;
    --teal: #2fb3b0;
    --violet: #8a76c9;
    --photo-dark: #4a3f3b;
    --photo-mid: #caa08a;
    --photo-light: #7fae63;
    --white: #ffffff;
  }
  html, body {
    margin: 0;
    padding: 0;
    width: 1200px;
    height: 1198px;
    overflow: hidden;
    background: var(--sky);
  }
  .cover {
    position: relative;
    width: 1200px;
    height: 1198px;
    background: var(--sky);
    font-family: "Archivo Black", "Arial Black", sans-serif;
  }
  .equalizer {
    position: absolute;
    left: 60px;
    bottom: 538px;
    display: flex;
    align-items: flex-end;
    gap: 24px;
  }
  .equalizer__bar {
    width: 90px;
    border-radius: 45px 45px 0 0;
  }
  .equalizer__bar--coral  { height: 300px; background: var(--coral); }
  .equalizer__bar--amber  { height: 460px; background: var(--amber); }
  .equalizer__bar--leaf   { height: 380px; background: var(--leaf); }
  .equalizer__bar--teal   { height: 520px; background: var(--teal); }
  .equalizer__bar--violet { height: 260px; background: var(--violet); }
  .host-photo {
    position: absolute;
    left: 700px;
    top: 70px;
    width: 440px;
    height: 590px;
    border-radius: 220px 220px 0 0;
    background: linear-gradient(160deg, var(--photo-dark) 0%, var(--photo-mid) 45%, var(--photo-light) 100%);
  }
  .title-panel {
    position: absolute;
    left: 0;
    top: 660px;
    width: 1200px;
    height: 538px;
    background: var(--ink);
    box-sizing: border-box;
    padding: 44px 60px 0;
  }
  .title {
    margin: 0;
    color: var(--white);
    font-weight: 400;
    line-height: 1;
  }
  .title__small {
    display: block;
    font-size: 88px;
    color: var(--amber);
    letter-spacing: 4px;
  }
  .title__large {
    display: block;
    font-size: 184px;
    line-height: 0.98;
    letter-spacing: -2px;
    white-space: nowrap;
  }
</style>
</head>
<body>
<main class="cover">
  <div class="equalizer" aria-hidden="true">
    <span class="equalizer__bar equalizer__bar--coral"></span>
    <span class="equalizer__bar equalizer__bar--amber"></span>
    <span class="equalizer__bar equalizer__bar--leaf"></span>
    <span class="equalizer__bar equalizer__bar--teal"></span>
    <span class="equalizer__bar equalizer__bar--violet"></span>
  </div>
  <div class="host-photo" role="img" aria-label="Cut-out photo of the host, smiling, in a hoodie and checked shirt"></div>
  <section class="title-panel">
    <h1 class="title">
      <span class="title__small">THE</span>
      <span class="title__large">DAVE R</span>
      <span class="title__large">HOUR</span>
    </h1>
  </section>
</main>
</body>
</html>
```